Business Card Design Project

Hello Designers, hope you are all aiming enjoy the weekend
I have the Business Logo (uploaded), you can alter the color which ever way you think would work,
Im looking for a simple yet striking feel, something which will stay memorable (I have uploaded 3 examples for you to flick through)
Information on the card, will just be the bare minimum,
Double Sided
Info being
i.e.
Name
Number
Website
ABN
Teo Marlowick
+482710365 (singapore)
+615093284 (Australia)
+790428153 (America)
www.lumoren-match.example
ABN 90817263
Enjoy,
Teo

```html
<!DOCTYPE html>
<html lang="en">
<head>
<meta charset="UTF-8">
<title>Lumoren Match — Business Card</title>
<link rel="stylesheet" href="https://fonts.googleapis.com/css2?family=Ubuntu:wght@400;500&family=Ubuntu+Mono&display=swap">
<style>
  :root {
    --page-bg: #e4e4e4;
    --card-bg: #ffffff;
    --card-edge: #d6d6d6;
    --brand-red: #c8102e;
    --brand-red-deep: #9e1020;
    --brand-grey: #55585c;
    --band-slate: #5c6670;
    --band-text: #ffffff;
    --divider: #c9cdd1;
  }
  * { box-sizing: border-box; margin: 0; padding: 0; }
  html, body {
    width: 1200px;
    height: 951px;
    overflow: hidden;
    background: var(--page-bg);
  }
  .canvas {
    position: relative;
    width: 1200px;
    height: 951px;
  }
  .card {
    position: absolute;
    width: 600px;
    height: 350px;
    background: var(--card-bg);
    border: 1px solid var(--card-edge);
    border-radius: 22px;
    overflow: hidden;
  }
  .card--front { left: 140px; top: 100px; }
  .card--back  { left: 460px; top: 500px; }

  /* Front */
  .brand {
    position: absolute;
    inset: 0;
    display: flex;
    align-items: center;
    justify-content: center;
    gap: 18px;
  }
  .brand__mark {
    width: 48px;
    height: 48px;
    background: var(--brand-red);
    border-radius: 8px;
  }
  .brand__name {
    font-family: "Ubuntu", sans-serif;
    font-weight: 500;
    font-size: 56px;
    letter-spacing: 0.5px;
    color: var(--brand-grey);
  }

  /* Back */
  .contact-band {
    position: absolute;
    left: 0;
    right: 0;
    top: 118px;
    height: 118px;
    display: flex;
    background: var(--band-slate);
  }
  .contact-band__name {
    width: 250px;
    background: linear-gradient(90deg, var(--brand-red-deep), var(--brand-red));
    display: flex;
    flex-direction: column;
    justify-content: center;
    align-items: flex-end;
    padding-right: 16px;
    font-family: "Ubuntu", sans-serif;
    font-size: 20px;
    line-height: 1.2;
    letter-spacing: 0.5px;
    text-transform: uppercase;
    color: var(--band-text);
  }
  .contact-band__details {
    position: relative;
    padding: 12px 0 0 34px;
    font-family: "Ubuntu Mono", monospace;
    font-size: 15px;
    line-height: 1.28;
    color: var(--band-text);
    list-style: none;
  }
  .contact-band__details::before {
    content: "";
    position: absolute;
    left: 14px;
    top: 14px;
    bottom: 14px;
    width: 1px;
    background: var(--divider);
  }
</style>
</head>
<body>
  <main class="canvas">
    <section class="card card--front" aria-label="Card front">
      <div class="brand">
        <span class="brand__mark" aria-hidden="true"></span>
        <span class="brand__name">Lumoren Match</span>
      </div>
    </section>

    <section class="card card--back" aria-label="Card back">
      <div class="contact-band">
        <div class="contact-band__name">
          <span>Teo</span>
          <span>Marlowick</span>
        </div>
        <ul class="contact-band__details">
          <li>+482710365 (singapore)</li>
          <li>+615093284 (Australia)</li>
          <li>+790428153 (America)</li>
          <li>www.lumoren-match.example</li>
          <li>ABN 90817263</li>
        </ul>
      </div>
    </section>
  </main>
</body>
</html>
```